Progressive business consultancy seeking innovative and clever powerpoint design

Were looking for a PowerPoint design for our Melbourne based business consulting company, Vantora.

About Us:
Based in Melbourne, Australia, Vantora is a management consulting organisation that partners with their clients to lead the execution of strategic process and system improvement initiatives.

Vantora offers business advisory services in Project Management, Business Process Management, Change Management, Business Analysis and Business Intelligence. Vantora combines hands on delivery with coaching in best practice methodologies and approaches to build our clients capabilities ensuring their ongoing success in project implementations.

Vantora has extensive experience across a wide range of industries. We specialise in assisting organisations across the accounting, legal, financial services and health sectors.

Our core purpose is to help businesses in the middle market navigate transformational change through clear and focused execution and enablement.

www.vantora.com.au
@vantora_hq

What we're looking for:
A PowerPoint template consisting of:
- a front/cover page with hero image (attached)
- a contents page
- a divider page (for different segments of the slide deck)
- a standard PowerPoint content page
- a blank PowerPoint page. (still Vantora themed)

The Vantora colours are white and blue (RGB:0/86/162 and
CMYK 97/73/4/0)

All slides should have the Vantora logo (attached) and a professional, almost corporate, (but not boring) theme that is consistent across all slides. The design should reflect our focus on the "e" in vantora, which is what we're really about - "e"xecution and "e"nablement of change.

I've attached a PNG file of our word template which shows the focus on the "e" as a watermark on the document as well as the font files if required.

Let me know if you need any further information or design specifics.

Thanks,

Marjorie
(on behalf of Desmond)
Updates

Project Deadline Extended
Reason: Hi Designers, We have received some really great designs. Thanks for taking the time to make your submissions. We have decided to extend the deadline as we need some more time to review and consult other colleagues on the great submissions we have received. We are also hoping we might get some additional submissions over the weekend. We would also like enough time to provide feedback on all the submissions received. Thanks for helping us out with some really creative work. Desmond @vantora_hq

Project Deadline Extended
Reason: Hi designers, thanks for taking the time to submit your designs. We have some really great submissions. We are going to have to extend our deadline again as we just haven't had the chance to review and provide feedback on all the designs. We will be closing this project off on Tuesday March 17. Thanks Desmond @vantora_hq

Target Market(s)

C-Level executives (CEO,COO,CIO) at professional services firms (Accounting and Legal), not for profit organisations and financial services firms.

Industry/Entity Type

Management Consulting

Font styles to use
Serif
Other font styles liked:
• Calibri or attached fonts

Requirements
Must have
• A PowerPoint template consisting of:
• 1) a front/cover page with hero image (attached)
• 2) a contents page
• 3) a divider page (for different segments of the slide deck)
• 4) a standard PowerPoint content page
• 5) a blank PowerPoint page. (still Vantora themed)
• 6) Two content
• 7) Comparison
• 8) Table
• 9) Picture column
• 10) Chevron
• The Vantora colours are white and blue (RGB:0/86/162 and
• CMYK 97/73/4/0)

```html
<!DOCTYPE html>
<html lang="en">
<head>
<meta charset="utf-8">
<title>Vantora – Who we are</title>
<link rel="stylesheet" href="https://fonts.googleapis.com/css2?family=Source+Sans+3:wght@300;400;700&display=swap">
<style>
  :root {
    --brand-blue: #0056a2;
    --brand-navy: #1b2a66;
    --ink-grey: #555a60;
    --kicker-grey: #8c8f93;
    --panel-white: #ffffff;
    --tab-dark: #3a3a3c;
    --bg-light: #f4f4f5;
    --bg-mid: #e6e7e9;
  }
  * { box-sizing: border-box; margin: 0; padding: 0; }
  html, body { width: 1200px; height: 675px; overflow: hidden; }
  body { font-family: "Source Sans 3", sans-serif; font-weight: 300; color: var(--ink-grey); }

  .slide { position: relative; width: 1200px; height: 675px; overflow: hidden; }

  .slide-backdrop {
    position: absolute; inset: 0;
    background: linear-gradient(120deg, var(--bg-light) 0%, #f1f1f2 45%, var(--bg-mid) 100%);
  }

  .kicker {
    position: absolute; left: 97px; top: 64px;
    font-size: 17px; letter-spacing: 0.2px; color: var(--kicker-grey);
  }
  .slide-title {
    position: absolute; left: 94px; top: 104px;
    font-size: 76px; font-weight: 300; color: var(--brand-blue); letter-spacing: -0.5px;
  }

  .intro { position: absolute; left: 97px; top: 0; width: 640px; }
  .intro p {
    position: absolute; left: 0; width: 640px;
    font-size: 23.5px; line-height: 30px; color: var(--ink-grey);
  }
  .intro strong { font-weight: 700; color: var(--brand-blue); }
  .intro .p1 { top: 219px; }
  .intro .p2 { top: 291px; }
  .intro .p3 { top: 363px; }
  .intro .p4 { top: 448px; }

  .principles-panel {
    position: absolute; left: 788px; top: 121px; width: 362px; height: 412px;
    background: var(--panel-white);
  }
  .principles-lead {
    position: absolute; left: 50px; top: 43px;
    font-size: 20px; line-height: 29px; color: var(--ink-grey);
  }
  .principle {
    position: absolute; left: 50px; display: flex; align-items: flex-start;
  }
  .principle-badge { width: 38px; height: 38px; flex: none; }
  .principle-label {
    margin-left: 19px; font-size: 25px; line-height: 28px; color: var(--brand-blue);
    padding-top: 5px;
  }
  .principle-1 { top: 129px; }
  .principle-2 { top: 189px; }
  .principle-3 { top: 249px; }
  .principle-4 { top: 309px; }

  .footer-band {
    position: absolute; left: 25px; top: 613px; width: 854px; height: 43px;
    background: var(--brand-blue); border-radius: 22px 0 0 22px;
    color: #fff; font-size: 16px; font-weight: 400; line-height: 43px; padding-left: 24px;
  }
  .brand-name {
    position: absolute; left: 906px; top: 613px; height: 43px; line-height: 43px;
    font-size: 36px; font-weight: 400; color: var(--brand-blue); letter-spacing: 0.5px;
  }
  .page-tab {
    position: absolute; left: 1101px; top: 613px; width: 74px; height: 43px;
    background: var(--tab-dark); border-radius: 0 22px 22px 0;
    color: #fff; font-weight: 700; font-size: 18px; line-height: 43px; text-align: center;
  }
</style>
</head>
<body>
<main class="slide">
  <div class="slide-backdrop" role="img" aria-label="Soft grey background with a faint connected-dots network pattern"></div>

  <p class="kicker">ANALYTICS FOR HIGH PERFORMANCE</p>
  <h1 class="slide-title">Who we are?</h1>

  <section class="intro">
    <p class="p1">At Vantora we offer a different kind of management consulting experience.</p>
    <p class="p2">We value our <strong>people</strong>, which is why we have the best talent available.</p>
    <p class="p3">We believe in <strong>partnering</strong> with our clients, enabling them to lead change.</p>
    <p class="p4">We focus on <strong>execution</strong>, which is why we don’t just leave our clients with a list of recommendations.</p>
  </section>

  <aside class="principles-panel">
    <p class="principles-lead">The business is founded on<br>four guiding principles.</p>

    <div class="principle principle-1">
      <svg class="principle-badge" viewBox="0 0 38 38" aria-hidden="true">
        <rect width="38" height="38" fill="#0056a2"/>
        <polygon points="20,8 26,8 38,20 38,38 30,38 20,28" fill="#1b2a66"/>
        <text x="16" y="28" font-family="Source Sans 3, sans-serif" font-weight="700" font-size="25" fill="#fff" text-anchor="middle">1</text>
      </svg>
      <span class="principle-label">EMBRACE CHANGE</span>
    </div>
    <div class="principle principle-2">
      <svg class="principle-badge" viewBox="0 0 38 38" aria-hidden="true">
        <rect width="38" height="38" fill="#0056a2"/>
        <polygon points="20,10 28,18 28,28 38,38 20,38 12,30" fill="#1b2a66"/>
        <text x="17" y="28" font-family="Source Sans 3, sans-serif" font-weight="700" font-size="25" fill="#fff" text-anchor="middle">2</text>
      </svg>
      <span class="principle-label">KEEP IT SIMPLE</span>
    </div>
    <div class="principle principle-3">
      <svg class="principle-badge" viewBox="0 0 38 38" aria-hidden="true">
        <rect width="38" height="38" fill="#0056a2"/>
        <polygon points="24,12 28,18 26,26 38,38 20,38 12,30" fill="#1b2a66"/>
        <text x="17" y="28" font-family="Source Sans 3, sans-serif" font-weight="700" font-size="25" fill="#fff" text-anchor="middle">3</text>
      </svg>
      <span class="principle-label">BE YOURSELF</span>
    </div>
    <div class="principle principle-4">
      <svg class="principle-badge" viewBox="0 0 38 38" aria-hidden="true">
        <rect width="38" height="38" fill="#0056a2"/>
        <polygon points="22,8 26,8 28,22 38,32 38,38 24,38 10,24" fill="#1b2a66"/>
        <text x="17" y="28" font-family="Source Sans 3, sans-serif" font-weight="700" font-size="25" fill="#fff" text-anchor="middle">4</text>
      </svg>
      <span class="principle-label">CHALLENGE THE<br>STATUS QUO</span>
    </div>
  </aside>

  <footer>
    <div class="footer-band">©2015 Vantora , Management Consulting - Melbourne</div>
    <div class="brand-name">Vantora</div>
    <div class="page-tab">2</div>
  </footer>
</main>
</body>
</html>
```